new business card and logo for a high end Automotive repair and performance shop

Need to update our design for our business cards. New address, and want a new look. I'll upload some pics of our current card. We are a high end auto repair/tuning shop. New address will be 5192 W. Larkfield Ave Brannock, T.X. 70418. I do have the vector files if needed. The logo would have a similar design. Love the look of carbon fiber, and brushed aluminum, although may have issues showing the texture of the material due to dpi restrictions during card printing. Also the logo would have to be easily printed on shirts, and for embroidery. Thanks, and good luck.

www.motor-zenith.example

Target Market(s)

High end automotive repair, dealership alternative.

Industry/Entity Type

Automotive

Contact Information for Business Card

MOTORZENITH
5192 W. LARKFIELD AVE
BRANNOCK, T.X. 70418
PH 555-307-9261
FAX 555-307-4470
EMAIL INFO@MOTOR-ZENITH.EXAMPLE

Logo Text

MotorZenith

Font styles to use
Sans Serif

Requirements
Must have
• name, address, description that was uploaded.
Nice to have
• maybe some brands i.e. vardo, orvex, Talvani, qrt, solvanta, dovik etc. not necessary. simple is good, like the look of carbon fiber, brushed aluminum.
Should not have
• open to all suggestions.

```html
<!DOCTYPE html>
<html lang="en">
<head>
<meta charset="utf-8">
<title>MotorZenith Business Card</title>
<link href="https://fonts.googleapis.com/css2?family=Open+Sans:wght@400;600;700&display=swap" rel="stylesheet">
<style>
  :root {
    --brand-red: #e2062b;
    --card-white: #f7f7f7;
    --rule-dark: #3a3a3a;
    --backdrop: #e9e6e1;
    --ink-white: #ffffff;
  }
  * { margin: 0; padding: 0; box-sizing: border-box; }
  html, body {
    width: 1200px; height: 900px; overflow: hidden;
    background: var(--backdrop);
    font-family: "Open Sans", Arial, sans-serif;
  }
  .stage { position: relative; width: 1200px; height: 900px; }
  .card {
    position: absolute; width: 640px; height: 366px;
    box-shadow: 0 6px 18px rgba(0,0,0,0.18);
    overflow: hidden;
  }
  /* Front */
  .card-front {
    left: 90px; top: 60px;
    background: var(--brand-red);
    display: flex; flex-direction: column; align-items: center; justify-content: center;
    color: var(--ink-white);
  }
  .front-wordmark {
    font-weight: 700; font-size: 52px; letter-spacing: -0.5px;
    color: var(--ink-white);
  }
  .front-tagline {
    margin-top: 30px; text-align: center;
    font-weight: 600; font-size: 15px; line-height: 1.45; letter-spacing: 1.2px;
    text-transform: uppercase;
  }
  /* Back */
  .card-back {
    left: 470px; top: 474px;
    background: var(--brand-red);
  }
  .back-top {
    position: absolute; left: 0; top: 0; width: 100%; height: 176px;
    background: var(--card-white);
    display: flex; align-items: center; justify-content: center;
  }
  .back-wordmark {
    font-weight: 700; font-size: 54px; letter-spacing: -0.5px;
    color: var(--brand-red);
    margin-top: 10px;
  }
  .back-rule {
    position: absolute; left: 0; top: 176px; width: 100%; height: 14px;
    background: var(--card-white);
    border-top: 4px solid var(--rule-dark);
  }
  .contact-list {
    position: absolute; right: 28px; top: 206px;
    list-style: none; text-align: right; color: var(--ink-white);
    font-size: 14px; line-height: 22px;
  }
  .contact-list li { display: flex; justify-content: flex-end; align-items: center; gap: 8px; }
  .contact-list svg { width: 12px; height: 12px; fill: var(--ink-white); }
  .person {
    position: absolute; left: 32px; top: 212px; color: var(--ink-white);
  }
  .person-name { font-weight: 700; font-size: 22px; line-height: 1.1; }
  .person-role { font-size: 15px; margin-top: 2px; }
  .address {
    position: absolute; left: 32px; top: 290px; color: var(--ink-white);
    font-size: 18px; line-height: 1.4; font-style: normal;
  }
</style>
</head>
<body>
<main class="stage">
  <section class="card card-front" aria-label="Card front">
    <div class="front-wordmark">MotorZenith</div>
    <p class="front-tagline">Specializing in Asian, European and<br>domestic vehicle repair, service<br>fabrication and performance</p>
  </section>

  <section class="card card-back" aria-label="Card back">
    <div class="back-top"><div class="back-wordmark">MotorZenith</div></div>
    <div class="back-rule"></div>

    <div class="person">
      <div class="person-name">Dana Whitcombe</div>
      <div class="person-role">Owner</div>
    </div>
    <address class="address">
      5192 W. Larkfield Ave ste B<br>Brannock, T.X. 70418
    </address>

    <ul class="contact-list">
      <li>1-555-307-9261
        <svg viewBox="0 0 24 24" aria-hidden="true"><path d="M6.6 10.8a15.1 15.1 0 0 0 6.6 6.6l2.2-2.2c.3-.3.7-.4 1-.2 1.1.4 2.3.6 3.6.6.6 0 1 .4 1 1V20c0 .6-.4 1-1 1A17 17 0 0 1 3 4c0-.6.4-1 1-1h3.5c.6 0 1 .4 1 1 0 1.3.2 2.5.6 3.6.1.3 0 .7-.2 1z"/></svg>
      </li>
      <li>1-555-307-4470
        <svg viewBox="0 0 24 24" aria-hidden="true"><path d="M6 2h10v5H6zM4 8h16a2 2 0 0 1 2 2v8h-4v4H6v-4H2v-8a2 2 0 0 1 2-2zm4 8v4h8v-4z"/></svg>
      </li>
      <li>info@motor-zenith.example
        <svg viewBox="0 0 24 24" aria-hidden="true"><path d="M2 5h20v14H2zm2 2v.5l8 5 8-5V7z"/></svg>
      </li>
      <li>www.motor-zenith.example
        <svg viewBox="0 0 24 24" aria-hidden="true"><circle cx="12" cy="12" r="10"/></svg>
      </li>
    </ul>
  </section>
</main>
</body>
</html>
```